The Hearth Guard Expert needs a Wordpress site for Home, Life and Safety Emergencies

NEED CUSTOM THEME FILES FOR WORDPRESS ncluded. I need a wordpress website that I will be able to edit down the road. Content wise the site I was trying to build is accurate. http://www.hearthguardexpert.example The site focuses on life, safety and home emergencies. My target audience is the first time home buyer. Usually in mid 20's think engineering type person.

I am up for a complete redesign. I want it to look clean and neat.

Things I need to have on the site :

- 2 Menus - A main menu and a secondary menu at top of page
- Search Bar in one of the main menus
- Social Media Share Buttons on one of the menus
- I am up for a color change (Maybe something a little softer) Need Help
- Main Page should be set up as a main page with separate blog page
- Need a CTA / Sign up for newsletter on page (location can vary)
- Blog Categories: When clicked need to show the full article and image.
- If you click on my home safety you will see how they are set up as a grid. I do not like this I want them to be easy to read and flow in order.

The site is going to mainly provide information for First Time Home Buyers. Eventually a page will be set up to sign up for a paid Home Safety Course. For now I want to focus on the content.

Mail should function with mail chimp for now.
This needs to be a functioning theme that I can edit. I currently have the rights to divi builder if that helps. I don't want to have to worry about the site I just want to focus on content creation.

Thank you

Target Market(s)

First Time Home Buyers Usually person in their 20's or 30's. Someone of the engineering, legal aid type mindset.

Industry/Entity Type

Safety

Coding

Coded - Design and coding required

Font styles to use
Serif
Sans Serif
Script

Colors

Designer to choose colors to be used in the design.

Requirements
Must have
• Wordpress integration.
• 2 Menus on top - Main and secondary
• Search function in a menu
• Social Media Icons in menu
• Sidebar with image of myself and some info on top , posts , categories
• Categories of blog posts need to list on the page. Not grid.
• Email signup on page at some part. (can be bottom, top or side. )
• Nice Clean state Front page.
• Color Combination that works well. (Doesn't have to be what is their now)
• Current links to site.
• Learn CPR needs to be a link to an external site ( http://www.rescueskillsnorthvale.example)
Nice to have
• I am flexible on the main page site design. I am not good at this so anything you feel. I cannot describe what I want but I will know it when I see it.
• I will come up with the information. Of course if any copy could be provided and shows value I would be willing to pay extra.
Should not have
• Grid Style for blog posts.
• Blog Posts should be in list style and each post for each category will just go down the page by order of date posted.

```html
<!DOCTYPE html>
<html lang="en">
<head>
<meta charset="utf-8">
<title>The Hearth Guard Expert</title>
<link href="https://fonts.googleapis.com/css2?family=Roboto:wght@400;500;700&family=Open+Sans:wght@400;600;700&display=swap" rel="stylesheet">
<style>
:root{
  --brown:#a3806a;
  --brown-dark:#8c6a55;
  --red:#ee4d4f;
  --ink:#2b2b2b;
  --body:#555;
  --muted:#888;
  --line:#e3e3e3;
  --white:#fff;
}
*{box-sizing:border-box;margin:0;padding:0}
html,body{width:1200px;height:3010px;overflow:hidden;background:var(--white)}
body{font-family:"Open Sans",Arial,sans-serif;color:var(--body);position:relative}
a{color:inherit;text-decoration:none}

/* top bar */
.topbar{position:absolute;top:0;left:0;width:1200px;height:28px;background:var(--brown);display:flex;align-items:center;justify-content:space-between;padding:0 98px}
.topbar .social{display:flex;gap:12px}
.topbar .social span{width:11px;height:11px;border-radius:50%;background:var(--white);display:block;opacity:.9}
.topbar .secondary{display:flex;font-size:11px;font-weight:600;color:var(--white)}
.topbar .secondary a{padding:0 8px;border-left:1px solid rgba(255,255,255,.5)}
.topbar .secondary a:first-child{border-left:0}

/* header */
.header{position:absolute;top:28px;left:0;width:1200px;height:80px;background:var(--white)}
.brand-disc{position:absolute;top:-10px;left:76px;width:176px;height:176px;border-radius:50%;background:var(--white);z-index:3;display:flex;align-items:center;justify-content:center}
.brand-name{font-family:"Roboto",Arial,sans-serif;font-weight:700;color:var(--red);font-size:25px;line-height:1.05;text-align:center;text-transform:uppercase;width:130px}
.main-nav{position:absolute;right:98px;top:0;height:80px;display:flex;align-items:center;gap:30px;font-family:"Roboto",Arial,sans-serif;font-weight:700;font-size:14px;color:var(--ink)}

/* hero */
.hero{position:absolute;top:108px;left:0;width:1200px;height:448px;background:linear-gradient(180deg,#9fb2c4 0%,#c9cfd2 35%,#8a8f83 60%,#5f7a3f 82%,#6f9a3e 100%)}
.hero h1{position:absolute;top:150px;left:0;width:100%;text-align:center;font-family:"Roboto",Arial,sans-serif;font-weight:700;font-size:58px;line-height:78px;color:var(--white);text-shadow:0 2px 6px rgba(0,0,0,.35)}
.hero .dots{position:absolute;top:390px;left:0;width:100%;display:flex;justify-content:center;gap:6px}
.hero .dots i{width:11px;height:11px;border-radius:50%;border:2px solid var(--white);display:block}
.hero .dots i.on{background:var(--white)}

/* intro */
.intro{position:absolute;top:606px;left:98px;width:582px}
.intro h2{font-family:"Roboto",Arial,sans-serif;font-weight:500;font-size:24px;line-height:40px;color:var(--ink);text-transform:uppercase}
.intro .photo{margin-top:30px;height:286px;border:4px solid #f1f1f1;background:linear-gradient(180deg,#b8a99a 0%,#e7c890 45%,#8a8a80 100%)}
.facts{list-style:none;margin-top:52px}
.facts li{display:flex;align-items:center;gap:12px;height:40px;font-size:12.5px;color:#555}
.facts svg{flex:none}
.tags{margin-top:34px;display:flex;flex-wrap:wrap;gap:18px 16px}
.tags a{border:2px solid var(--line);padding:0 22px;height:42px;display:flex;align-items:center;font-family:"Roboto",Arial,sans-serif;font-weight:500;font-size:15px;color:var(--brown);text-transform:uppercase}
.tags a.more{font-size:12px;color:var(--red);font-weight:700;padding:0 18px}

/* sidebar */
.profile{position:absolute;top:612px;left:720px;width:378px;height:380px;background:var(--red);border:5px solid #f0f0f0;text-align:center;color:var(--white)}
.profile .avatar{width:112px;height:112px;border-radius:50%;border:4px solid var(--white);background:linear-gradient(180deg,#c9c2bc,#8d8a8a);margin:24px auto 0}
.profile h3{font-family:"Roboto",Arial,sans-serif;font-weight:700;font-size:17px;margin-top:26px;text-transform:uppercase}
.profile .role{font-style:italic;font-weight:600;font-size:12px;margin-top:6px}
.profile p{font-size:11.5px;line-height:22px;margin:18px 34px 0}
.profile .social{display:flex;justify-content:center;gap:14px;margin-top:18px}
.profile .social span{width:28px;height:28px;border-radius:50%;background:var(--white);display:block}

.recent{position:absolute;top:1032px;left:720px;width:378px;height:488px;border:2px solid var(--line)}
.recent h3{background:var(--brown);color:var(--white);font-family:"Roboto",Arial,sans-serif;font-weight:500;font-size:19px;height:46px;line-height:46px;padding-left:20px;text-transform:uppercase}
.post{display:flex;gap:18px;padding:18px 20px 0 20px;height:96px}
.post .thumb{width:96px;height:76px;flex:none}
.post h4{font-family:"Roboto",Arial,sans-serif;font-weight:500;font-size:14px;color:var(--ink);line-height:22px;width:200px}
.post time{display:flex;align-items:center;gap:6px;font-size:11px;color:var(--muted);margin-top:6px}
.recent .view{position:absolute;left:22px;bottom:18px;font-size:11px;font-weight:700;color:var(--red)}

.divider{position:absolute;top:1578px;left:98px;width:1000px;height:1px;background:var(--line)}

/* blog grid */
.blog-title{position:absolute;top:1630px;left:0;width:1200px;text-align:center;font-family:"Roboto",Arial,sans-serif;font-weight:700;font-size:25px;color:var(--ink);text-transform:uppercase}
.cards{position:absolute;top:1716px;left:98px;width:1000px;display:grid;grid-template-columns:repeat(3,314px);column-gap:29px;row-gap:64px}
.card{height:382px;border:2px solid var(--line);position:relative;text-align:center;background:var(--white)}
.card .media{height:210px}
.card .badge{position:absolute;top:172px;left:50%;margin-left:-37px;width:74px;height:74px;border-radius:50%;background:var(--brown);border:3px solid var(--white);display:flex;align-items:center;justify-content:center}
.card h3{font-family:"Roboto",Arial,sans-serif;font-weight:500;font-size:18px;line-height:22px;color:var(--ink);margin-top:60px;text-transform:uppercase}
.card p{font-size:11.5px;line-height:24px;color:#666;margin:10px 22px 0}
.card .read{position:absolute;left:50%;bottom:-18px;transform:translateX(-50%);background:var(--white);border:2px solid var(--line);border-radius:20px;padding:0 14px;height:34px;line-height:30px;font-size:11px;font-weight:700;color:var(--red);white-space:nowrap}

/* footer */
.footer{position:absolute;top:2626px;left:0;width:1200px;height:384px;border-top:5px solid var(--brown)}
.footer .brand-name{position:absolute;top:82px;left:98px;width:196px;font-size:34px;line-height:1.05}
.footer .col{position:absolute;top:66px}
.footer h4{font-family:"Roboto",Arial,sans-serif;font-weight:700;font-size:16px;color:var(--ink);text-transform:uppercase;margin-bottom:18px}
.footer .links a{display:block;font-size:11.5px;line-height:25px;color:#555}
.footer .news p{font-size:11.5px;line-height:22px;color:#555;width:220px}
.footer .news .field{margin-top:18px;width:254px;border-bottom:1px solid #ccc;font-size:10.5px;color:#999;padding:6px 14px}
.footer .news .btn{display:inline-block;margin-top:20px;background:var(--red);color:var(--white);font-size:10.5px;font-weight:700;border-radius:16px;padding:0 16px;height:30px;line-height:30px}
.footer .contact li{list-style:none;display:flex;gap:18px;font-size:11.5px;line-height:20px;color:#555;margin-bottom:16px}
.footer .contact svg{flex:none;margin-top:3px}
.footer .bottom{position:absolute;top:292px;left:98px;width:1000px;border-top:1px solid var(--line);display:flex;justify-content:space-between;align-items:center;padding-top:22px;font-size:11px;color:#555}
.footer .bottom .social{display:flex;gap:8px}
.footer .bottom .social span{width:28px;height:28px;border-radius:50%;border:2px solid #d9c9bd;display:block}
</style>
</head>
<body>

<div class="topbar">
  <div class="social"><span></span><span></span><span></span><span></span></div>
  <nav class="secondary"><a href="#">Home Safety</a><a href="#">Life Safety</a><a href="#">Fire Safety</a><a href="#">Pet Safety</a><a href="#">Safety Saturday</a></nav>
</div>

<header class="header">
  <div class="brand-disc"><span class="brand-name">The Hearth Guard Expert</span></div>
  <nav class="main-nav">
    <a href="#">HOME</a><a href="#">ABOUT ME</a><a href="#">SAFETY INFO</a><a href="#">LEARN CPR</a><a href="#">PREVENT HOME DISASTERS</a><a href="#">CONTACT ME</a>
    <svg width="14" height="14" viewBox="0 0 14 14"><circle cx="5.5" cy="5.5" r="4.3" fill="none" stroke="#2b2b2b" stroke-width="2"/><line x1="8.6" y1="8.6" x2="13" y2="13" stroke="#2b2b2b" stroke-width="2.2"/></svg>
  </nav>
</header>

<section class="hero" role="img" aria-label="Photo of a two-storey suburban house with a porch, green lawn and flower beds">
  <h1>KNOW SAFETY.<br>DISASTER NEVER SLEEPS</h1>
  <div class="dots"><i class="on"></i><i></i><i></i><i></i></div>
</section>

<section class="intro">
  <h2>Want to protect your home or loved one from an emergency ? Have you had a home emergency ? Not sure what to do ?</h2>
  <div class="photo" role="img" aria-label="Photo of two hands sheltering a small wooden house model against a sunset"></div>
  <ul class="facts">
    <li><svg width="13" height="13" viewBox="0 0 13 13"><circle cx="6.5" cy="6.5" r="6.5" fill="#ee4d4f"/><path d="M3.5 6.7l2 2 4-4.2" stroke="#fff" stroke-width="1.6" fill="none"/></svg>House Fires Kill 8 People every day.</li>
    <li><svg width="13" height="13" viewBox="0 0 13 13"><circle cx="6.5" cy="6.5" r="6.5" fill="#ee4d4f"/><path d="M3.5 6.7l2 2 4-4.2" stroke="#fff" stroke-width="1.6" fill="none"/></svg>Flood damage accounts for $14.3 Billon in Property Damage Yearly.</li>
    <li><svg width="13" height="13" viewBox="0 0 13 13"><circle cx="6.5" cy="6.5" r="6.5" fill="#ee4d4f"/><path d="M3.5 6.7l2 2 4-4.2" stroke="#fff" stroke-width="1.6" fill="none"/></svg>Disaster Never Sleeps and Always strikes at the Worst possible time.</li>
    <li><svg width="13" height="13" viewBox="0 0 13 13"><circle cx="6.5" cy="6.5" r="6.5" fill="#ee4d4f"/><path d="M3.5 6.7l2 2 4-4.2" stroke="#fff" stroke-width="1.6" fill="none"/></svg>Be Prepared. Know What to do.</li>
    <li><svg width="13" height="13" viewBox="0 0 13 13"><circle cx="6.5" cy="6.5" r="6.5" fill="#ee4d4f"/><path d="M3.5 6.7l2 2 4-4.2" stroke="#fff" stroke-width="1.6" fill="none"/></svg>I am here for you.</li>
    <li><svg width="13" height="13" viewBox="0 0 13 13"><circle cx="6.5" cy="6.5" r="6.5" fill="#ee4d4f"/><path d="M3.5 6.7l2 2 4-4.2" stroke="#fff" stroke-width="1.6" fill="none"/></svg>As an Emergency Services Professional I want to share what I have seen and how to Help.</li>
    <li><svg width="13" height="13" viewBox="0 0 13 13"><circle cx="6.5" cy="6.5" r="6.5" fill="#ee4d4f"/><path d="M3.5 6.7l2 2 4-4.2" stroke="#fff" stroke-width="1.6" fill="none"/></svg>We all have busy lives. Preparing NOW will Save you Time, Money and could Save A Life.</li>
  </ul>
  <div class="tags">
    <a href="#">Fire Safety</a><a href="#">Home Safety Tips</a><a href="#">Uncategorized</a><a href="#">Safety Saturday Posts</a><a href="#" class="more">VIEW MORE</a>
  </div>
</section>

<aside class="profile">
  <div class="avatar" role="img" aria-label="Portrait photo of the site author"></div>
  <h3>Dorian Vasquell</h3>
  <div class="role">About The Hearth Guard Expert</div>
  <p>I provide common sense advice to help prevent the headache of a typical home problem, which left unattended will be come an emergency. Things come up especially if you own or rent a house.</p>
  <div class="social"><span></span><span></span><span></span></div>
</aside>

<aside class="recent">
  <h3>Recent Posts</h3>
  <div class="post"><div class="thumb" role="img" aria-label="Post image about smoke detectors" style="background:#6e4a35"></div><div><h4>Safety Saturday — Escape Plan</h4><time><svg width="10" height="10" viewBox="0 0 10 10"><rect x="0.5" y="1.5" width="9" height="8" fill="none" stroke="#ee4d4f"/><line x1="0.5" y1="4" x2="9.5" y2="4" stroke="#ee4d4f"/></svg>17/05/2017</time></div></div>
  <div class="post"><div class="thumb" role="img" aria-label="Post image about a fire escape plan" style="background:#7a4a32"></div><div><h4>Safety Saturday — Smoke Detector</h4><time><svg width="10" height="10" viewBox="0 0 10 10"><rect x="0.5" y="1.5" width="9" height="8" fill="none" stroke="#ee4d4f"/><line x1="0.5" y1="4" x2="9.5" y2="4" stroke="#ee4d4f"/></svg>17/05/2017</time></div></div>
  <div class="post"><div class="thumb" role="img" aria-label="Post image about CPR training" style="background:linear-gradient(135deg,#3b5a9a,#d9d3cc)"></div><div><h4>Learn CPR</h4><time><svg width="10" height="10" viewBox="0 0 10 10"><rect x="0.5" y="1.5" width="9" height="8" fill="none" stroke="#ee4d4f"/><line x1="0.5" y1="4" x2="9.5" y2="4" stroke="#ee4d4f"/></svg>17/05/2017</time></div></div>
  <div class="post"><div class="thumb" role="img" aria-label="Post image about planning a fire escape" style="background:linear-gradient(135deg,#e8e2d8,#b03a2e)"></div><div><h4>Plan your Fire Escape – Surviving a House Fire</h4><time><svg width="10" height="10" viewBox="0 0 10 10"><rect x="0.5" y="1.5" width="9" height="8" fill="none" stroke="#ee4d4f"/><line x1="0.5" y1="4" x2="9.5" y2="4" stroke="#ee4d4f"/></svg>17/05/2017</time></div></div>
  <a href="#" class="view">VIEW MORE &gt;&gt;</a>
</aside>

<div class="divider"></div>

<h2 class="blog-title">Our Blog</h2>
<section class="cards">
  <article class="card">
    <div class="media" role="img" aria-label="Photo of many hands joined in a circle" style="background:linear-gradient(180deg,#f4f4f4,#c99a7c)"></div>
    <div class="badge"><svg width="28" height="28" viewBox="0 0 28 28"><circle cx="14" cy="9" r="6" fill="#fff"/><path d="M3 27c0-7 5-11 11-11s11 4 11 11z" fill="#fff"/></svg></div>
    <h3>About Me</h3><p>I provide common sense advice to help prevent the headache of a typical home problem</p><a href="#" class="read">READ MORE &gt;&gt;</a>
  </article>
  <article class="card">
    <div class="media" role="img" aria-label="Photo of a hand holding a small model house on grass" style="background:linear-gradient(180deg,#e9f0e4,#7fa85a)"></div>
    <div class="badge"><svg width="30" height="28" viewBox="0 0 30 28"><path d="M15 2L2 14h4v12h7v-8h4v8h7V14h4z" fill="#fff"/></svg></div>
    <h3>Home Safety</h3><p>I provide common sense advice to help prevent the headache of a typical home problem</p><a href="#" class="read">READ MORE &gt;&gt;</a>
  </article>
  <article class="card">
    <div class="media" role="img" aria-label="Photo of CPR practice on a training manikin" style="background:linear-gradient(180deg,#b0282b,#e9b79a)"></div>
    <div class="badge"><svg width="30" height="28" viewBox="0 0 30 28"><path d="M15 26L4 15C0 11 2 3 8 3c3 0 5 2 7 4 2-2 4-4 7-4 6 0 8 8 4 12z" fill="#fff"/></svg></div>
    <h3>Life Safety</h3><p>I provide common sense advice to help prevent the headache of a typical home problem</p><a href="#" class="read">READ MORE &gt;&gt;</a>
  </article>
  <article class="card">
    <div class="media" role="img" aria-label="Photo of a desk with a laptop, charts and documents" style="background:linear-gradient(135deg,#5a6878,#c7ccd2)"></div>
    <div class="badge"><svg width="30" height="28" viewBox="0 0 30 28"><circle cx="11" cy="16" r="7" fill="none" stroke="#fff" stroke-width="4" stroke-dasharray="3 2.5"/><circle cx="11" cy="16" r="2.5" fill="#fff"/><circle cx="23" cy="7" r="4" fill="none" stroke="#fff" stroke-width="3" stroke-dasharray="2 2"/></svg></div>
    <h3>Resources</h3><p>I provide common sense advice to help prevent the headache of a typical home problem</p><a href="#" class="read">READ MORE &gt;&gt;</a>
  </article>
  <article class="card">
    <div class="media" role="img" aria-label="Photo of a person hugging a pet dog" style="background:linear-gradient(135deg,#8a6a55,#e4d9cc)"></div>
    <div class="badge"><svg width="28" height="28" viewBox="0 0 28 28"><ellipse cx="14" cy="19" rx="6" ry="5" fill="#fff"/><circle cx="6" cy="12" r="2.6" fill="#fff"/><circle cx="11" cy="7" r="2.6" fill="#fff"/><circle cx="17" cy="7" r="2.6" fill="#fff"/><circle cx="22" cy="12" r="2.6" fill="#fff"/></svg></div>
    <h3>Pet Safety</h3><p>I provide common sense advice to help prevent the headache of a typical home problem</p><a href="#" class="read">READ MORE &gt;&gt;</a>
  </article>
  <article class="card">
    <div class="media" role="img" aria-label="Photo of a fire extinguisher spraying at flames" style="background:linear-gradient(135deg,#f2b24a,#c8462a 60%,#e9e6e2)"></div>
    <div class="badge"><svg width="28" height="30" viewBox="0 0 28 30"><rect x="9" y="9" width="10" height="19" rx="3" fill="#fff"/><rect x="12" y="4" width="4" height="5" fill="#fff"/><path d="M16 5h7l2 4" stroke="#fff" stroke-width="2" fill="none"/></svg></div>
    <h3>Fire Safety</h3><p>I provide common sense advice to help prevent the headache of a typical home problem</p><a href="#" class="read">READ MORE &gt;&gt;</a>
  </article>
</section>

<footer class="footer">
  <span class="brand-name">The Hearth Guard Expert</span>
  <div class="col links" style="left:364px">
    <h4>Information</h4>
    <a href="#">Home</a><a href="#">About Me</a><a href="#">Safety Info</a><a href="#">Learn CPR</a><a href="#">Prevent Home Disasters</a><a href="#">Contact Me</a>
  </div>
  <div class="col news" style="left:560px">
    <h4>Newsletter Subscription</h4>
    <p>Register your Email Address to get Information about us</p>
    <div class="field">Email Address</div>
    <a href="#" class="btn">SUBSCRIBE</a>
  </div>
  <div class="col contact" style="left:878px">
    <h4>Contact Us</h4>
    <ul>
      <li><svg width="10" height="13" viewBox="0 0 10 13"><path d="M5 13S0 7.5 0 5a5 5 0 0110 0c0 2.5-5 8-5 8z" fill="#777"/><circle cx="5" cy="5" r="1.8" fill="#fff"/></svg><span>48 Larkfield Row #12<br>Northvale, NV 20450</span></li>
      <li><svg width="12" height="12" viewBox="0 0 12 12"><path d="M2 0l2.5 3-1.3 1.6c.8 1.7 2.1 3 3.8 3.8L8.6 7l3 2.5L10 12C4.5 11.5.5 7.5 0 2z" fill="#777"/></svg><span>1 555 010 2040</span></li>
      <li><svg width="13" height="12" viewBox="0 0 13 12"><rect x="0" y="4" width="13" height="8" fill="#777"/><rect x="3" y="0" width="7" height="5" fill="none" stroke="#777" stroke-width="1.4"/></svg><span>1 555 010 2041</span></li>
      <li><svg width="13" height="10" viewBox="0 0 13 10"><rect width="13" height="10" fill="#777"/><path d="M0 0l6.5 5L13 0" stroke="#fff" stroke-width="1.2" fill="none"/></svg><span>info@hearthguardexpert.example</span></li>
    </ul>
  </div>
  <div class="bottom">
    <span>Copyrights © 2017, The Hearth Guard Expert. All rights reserved. Terms &amp; Condition.</span>
    <div class="social"><span></span><span></span><span></span><span></span></div>
  </div>
</footer>

</body>
</html>
```